Brightwell - Self Development Mobile App

Basic Instructions
1. please create an android app screen design for me, in figma, for my new app “Brightwell” based on this pencil drawing (Subjects.jpg)
2. Create the color pallet based on the colors of the logo (#fcd354 and #5dc9b7) and also add shades based on these colors based on material design.
3. the background should be white.
4. Use material design
Get Inspired by wordhopper design and calmnest design
These are the directions i provided for the programmer on how this screen will work:
top bar:
back icon on left (show if you are in a category and press to go back one category)
name of the field in middle in bold
share icon for sharing the current subject on the right before the drop down menu
3 dot icon on the right (drop down menu)
2nd top bar:
fire icon on left for streak (how many days straight did you do a lesson)
star icon a bit after it (how many lessons did you pass)
circles section:
each category will get a section
each category will have a small star with a number that shows how many stars the user has from that category
each category will have an icon before it
under each category there will be circles for all the subjects under that category
scroll horizontally to see more subjects
each subject will have the amount stars gained from it (like the circles of the fields in the fields screen)
scroll down to see more fields with their subjects
note that the order of the subjects and categories should be based on the practial/spiritual score that the user has been assigned based on the initial wizard
More Notes
1. the scribbles in the circles under the following categories (Dreams, Sub-Concious, Feeling)) are just place filers. Please add example content based on the content in the circles that are under “Memory” category
2. There are more sections after Feeling so users should be able to scroll down to see more sections
3. There are more categories to the right so under each section
Final Thoughts
Maybe its better to have rounded cornered squares instead of circles. You choose what you think is best.
After you have created the Subjects screen and I like it, then I'll give you instructions for the other 5 screens.
Target Market(s)
general public, adults 18-80
Font styles to use
Look and feel
Each slider illustrates characteristics of the customer's brand and the style your logo design should communicate.

```html
<!DOCTYPE html>
<html lang="en">
<head>
<meta charset="utf-8">
<title>Brightwell – Self Development App Screens</title>
<link href="https://fonts.googleapis.com/css2?family=Roboto:wght@400;500;700&family=Rubik:wght@500;600;700&display=swap" rel="stylesheet">
<style>
  :root{
    --yellow:#fcd354;
    --teal:#5dc9b7;
    --canvas:#d3d4d6;
    --ink:#4a4a4a;
    --ink-dark:#222;
    --bar:#fbf6fc;
    --track:#e6e6e6;
    --white:#ffffff;
  }
  *{box-sizing:border-box;margin:0;padding:0}
  html,body{width:1200px;height:1200px;overflow:hidden;background:var(--canvas)}
  body{position:relative;font-family:'Roboto',sans-serif;color:var(--ink)}
  .phone{position:absolute;width:301px;height:670px;background:var(--white);overflow:hidden;transform:scale(0.621);transform-origin:0 0;box-shadow:0 0 0 1px #c9c9cc}
  .status{position:absolute;left:0;top:0;width:100%;height:50px}
  .status .time{position:absolute;left:17px;top:17px;font-size:10px;color:var(--ink-dark)}
  .status .camera{position:absolute;left:142px;top:14px;width:17px;height:17px;border-radius:50%;background:#1e1e1e}
  .status .signals{position:absolute;right:16px;top:18px}
  .appbar{position:absolute;left:0;top:50px;width:100%;height:46px;background:var(--bar);display:flex;align-items:center}
  .appbar .back{margin-left:14px;width:14px;height:14px}
  .appbar .title{margin-left:13px;font-size:16px;color:var(--ink-dark)}
  .appbar .share{position:absolute;right:14px;top:16px;width:14px;height:14px}
  .stats{position:absolute;right:22px;top:121px;display:flex;align-items:center;gap:14px;font-size:13px;font-weight:500}
  .stats span{display:flex;align-items:center;gap:4px}
  .stats .fire{color:var(--yellow)}
  .stats .stars{color:var(--teal)}
  .progress{position:absolute;left:15px;top:163px;width:269px;height:10px;border-radius:5px;background:var(--track)}
  .progress i{display:block;height:100%;border-radius:5px;background:var(--yellow)}
  .bubble{position:absolute;width:74px;height:74px;border-radius:50%;border:1.5px solid var(--teal);display:flex;flex-direction:column;align-items:center;justify-content:center;font-family:'Roboto',sans-serif;font-weight:500;font-size:8px;color:var(--teal);text-align:center;line-height:1.1;background:var(--white)}
  .bubble.filled{background:var(--teal);color:var(--white)}
  .bubble .dot{width:13px;height:13px;border-radius:50%;background:var(--yellow);margin-bottom:6px}
  .bubble .rate{margin-top:5px;font-size:8px}
  .me{position:absolute;left:106px;top:342px;width:88px;height:88px;border-radius:50%;background:var(--yellow);display:flex;align-items:center;justify-content:center;font-family:'Rubik',sans-serif;font-weight:600;font-size:24px;color:var(--ink)}
  .navpill{position:absolute;left:42px;top:605px;width:216px;height:47px;border-radius:24px;background:var(--teal);display:flex;justify-content:space-around;align-items:center}
  .screen-title{position:absolute;left:0;width:100%;top:118px;text-align:center;font-family:'Rubik',sans-serif;font-weight:500;font-size:20px;color:var(--ink)}
  .prompt{position:absolute;left:20px;width:261px;text-align:center;font-family:'Rubik',sans-serif;font-weight:600;font-size:24px;line-height:28px;color:var(--teal)}
  .kicker{position:absolute;left:60px;width:181px;text-align:center;font-size:9.5px;font-weight:700;line-height:12.5px;color:var(--ink-dark)}
  .corner{position:absolute;top:630px;width:22px;height:22px;border-radius:50%;background:#444;color:#fff;font-size:8px;font-weight:700;display:flex;align-items:center;justify-content:center}
  .next{position:absolute;left:83px;top:459px;width:128px;height:128px;border-radius:50%;background:var(--yellow);display:flex;align-items:center;justify-content:center;font-family:'Rubik',sans-serif;font-weight:600;font-size:22px;color:var(--ink)}
  .section-head{position:absolute;left:17px;top:178px;font-family:'Rubik',sans-serif;font-weight:600;font-size:24px;color:var(--teal)}
  .ring{position:absolute;left:245px;top:172px}
  .word-card{position:absolute;width:128px;height:139px;border-radius:3px;background:var(--yellow);display:flex;align-items:flex-end;justify-content:center;padding-bottom:12px;font-size:12px;font-weight:500;color:var(--ink)}
  .category{position:absolute;left:15px;width:286px}
  .category .name{position:absolute;left:0;top:0;font-family:'Rubik',sans-serif;font-weight:500;font-size:15px;color:var(--ink-dark)}
  .category .count{position:absolute;left:249px;top:-2px;font-size:8px;color:var(--ink-dark);display:flex;align-items:center;gap:2px}
  .lesson{position:absolute;top:23px;width:109px;height:83px;border-radius:3px;background:var(--teal);color:var(--white);font-size:11.5px;font-weight:700;line-height:13px;padding:0 10px 10px;display:flex;align-items:flex-end}
  .lesson .rate{position:absolute;right:8px;top:8px;font-size:7px;font-weight:500;display:flex;align-items:center;gap:2px}
  .answer{position:absolute;top:430px;width:73px;height:73px;border-radius:50%;background:var(--teal);color:var(--white);font-size:8px;font-weight:700;line-height:9px;display:flex;align-items:center;justify-content:center;text-align:center}
</style>
</head>
<body>

<svg width="0" height="0" style="position:absolute" aria-hidden="true">
  <defs>
    <symbol id="i-back" viewBox="0 0 14 14"><path d="M13 7H2M7 1.5L1.5 7 7 12.5" fill="none" stroke="#222" stroke-width="1.4"/></symbol>
    <symbol id="i-share" viewBox="0 0 14 14"><g fill="none" stroke="#222" stroke-width="1.1"><circle cx="11" cy="2.5" r="1.8"/><circle cx="3" cy="7" r="1.8"/><circle cx="11" cy="11.5" r="1.8"/><path d="M4.6 6.1L9.4 3.4M4.6 7.9l4.8 2.7"/></g></symbol>
    <symbol id="i-star" viewBox="0 0 24 24"><path d="M12 1.5l3.1 6.9 7.4.7-5.6 5 1.7 7.4L12 17.6l-6.6 3.9 1.7-7.4-5.6-5 7.4-.7z" fill="currentColor"/></symbol>
    <symbol id="i-fire" viewBox="0 0 24 24"><path d="M13 1c1 4 5 6 5 12a6 6 0 0 1-12 0c0-3 2-5 3-6 0 2 1 3 2 3 0-4 0-6 2-9z" fill="currentColor"/></symbol>
    <symbol id="i-signal" viewBox="0 0 36 12"><path d="M0 4a9 9 0 0 1 12 0L6 10z" fill="#ddd"/><path d="M24 11V1L14 11z" fill="#222"/><rect x="28" y="2" width="5" height="9" fill="#ddd"/><rect x="28" y="6" width="5" height="5" fill="#222"/></symbol>
    <symbol id="i-speaker" viewBox="0 0 22 22"><circle cx="11" cy="11" r="11" fill="#444"/><path d="M6 9h2.5L12 6v10l-3.5-3H6z" fill="#fff"/><path d="M14 8.5a3.5 3.5 0 0 1 0 5M15.5 7a5.5 5.5 0 0 1 0 8" fill="none" stroke="#fff" stroke-width="1"/></symbol>
  </defs>
</svg>

<!-- Screen: Wizard (map) -->
<section class="phone" style="left:268px;top:158px">
  <div class="status"><span class="time">4:07</span><span class="camera"></span><svg class="signals" width="36" height="12"><use href="#i-signal"/></svg></div>
  <header class="appbar"><svg class="back"><use href="#i-back"/></svg><span class="title">Wizard</span><svg class="share"><use href="#i-share"/></svg></header>
  <div class="stats"><span class="fire"><svg width="16" height="16"><use href="#i-fire"/></svg>2</span><span class="stars"><svg width="18" height="18"><use href="#i-star"/></svg>34</span></div>
  <div class="progress"><i style="width:90%"></i></div>
  <svg style="position:absolute;left:0;top:0" width="301" height="670" aria-hidden="true">
    <g stroke="#5dc9b7" stroke-width="1">
      <line x1="150" y1="386" x2="150" y2="278"/><line x1="150" y1="386" x2="227" y2="316"/>
      <line x1="150" y1="386" x2="247" y2="394"/><line x1="150" y1="386" x2="227" y2="472"/>
      <line x1="150" y1="386" x2="150" y2="510"/><line x1="150" y1="386" x2="74" y2="472"/>
      <line x1="150" y1="386" x2="51" y2="394"/><line x1="150" y1="386" x2="74" y2="316"/>
    </g>
  </svg>
  <div class="bubble" style="left:113px;top:241px"><i class="dot"></i>Recommended<span class="rate">★ 7</span></div>
  <div class="bubble" style="left:190px;top:279px"><i class="dot"></i>Body<span class="rate">★ 7</span></div>
  <div class="bubble" style="left:210px;top:357px"><i class="dot"></i>Finance</div>
  <div class="bubble" style="left:190px;top:435px"><i class="dot"></i>Professional</div>
  <div class="bubble" style="left:113px;top:473px"><i class="dot"></i>Social<span class="rate">★ 7</span></div>
  <div class="bubble" style="left:37px;top:435px"><i class="dot"></i>Spiritual</div>
  <div class="bubble" style="left:14px;top:357px"><i class="dot"></i>Hobbies<span class="rate">★ 7</span></div>
  <div class="bubble" style="left:37px;top:279px"><i class="dot"></i>Mind</div>
  <div class="me">Me</div>
  <nav class="navpill">
    <svg width="18" height="18" viewBox="0 0 18 18"><path d="M2 8l7-6 7 6v9H2z" fill="#fff"/><rect x="7" y="11" width="4" height="6" fill="#5dc9b7"/></svg>
    <svg width="18" height="18" viewBox="0 0 18 18" fill="#fff"><rect x="1" y="1" width="7" height="7" rx="1"/><circle cx="13.5" cy="4.5" r="3.5"/><rect x="1" y="10" width="7" height="7" rx="1"/><rect x="10" y="10" width="7" height="7" rx="1"/></svg>
    <svg width="18" height="18" viewBox="0 0 18 18" fill="#fff"><circle cx="9" cy="5" r="4"/><path d="M1 17c0-5 4-7 8-7s8 2 8 7z"/></svg>
  </nav>
</section>

<!-- Screen: Wizard (subject choice) -->
<section class="phone" style="left:504px;top:158px">
  <div class="status"><span class="time">4:07</span><span class="camera"></span><svg class="signals" width="36" height="12"><use href="#i-signal"/></svg></div>
  <header class="appbar"><svg class="back"><use href="#i-back"/></svg><span class="title">Wizard</span><svg class="share"><use href="#i-share"/></svg></header>
  <h1 class="screen-title">Brightwell</h1>
  <div class="progress"><i style="width:90%"></i></div>
  <p class="prompt" style="top:236px">Please choose three subjects that interest you the most</p>
  <div class="bubble" style="left:36px;top:349px">Subject<br>1</div>
  <div class="bubble" style="left:113px;top:385px">Subject<br>2</div>
  <div class="bubble" style="left:190px;top:349px">Subject<br>3</div>
  <div class="bubble filled" style="left:36px;top:427px">Subject<br>4</div>
  <div class="bubble" style="left:113px;top:465px">Subject<br>5</div>
  <div class="bubble filled" style="left:190px;top:427px">Subject<br>6</div>
  <div class="bubble" style="left:36px;top:505px">Subject<br>7</div>
  <div class="bubble filled" style="left:113px;top:543px">Subject<br>8</div>
  <div class="bubble" style="left:190px;top:505px">Subject<br>9</div>
  <span class="corner" style="left:14px">X1</span>
  <svg style="position:absolute;left:261px;top:630px" width="22" height="22"><use href="#i-speaker"/></svg>
</section>

<!-- Screen: Memory Remembering -->
<section class="phone" style="left:745px;top:158px">
  <div class="status"><span class="time">4:07</span><span class="camera"></span><svg class="signals" width="36" height="12"><use href="#i-signal"/></svg></div>
  <header class="appbar"><svg class="back"><use href="#i-back"/></svg><span class="title">Memory Remembering</span><svg class="share"><use href="#i-share"/></svg></header>
  <div class="stats"><span class="fire"><svg width="16" height="16"><use href="#i-fire"/></svg>2</span><span class="stars"><svg width="18" height="18"><use href="#i-star"/></svg>34</span></div>
  <div class="progress"><i style="width:60%"></i></div>
  <p class="prompt" style="top:236px;left:50px;width:201px">Exercise Text goes here. Two or three lines</p>
  <p class="kicker" style="top:330px">If it needs further explanation, a kicker of this font size would be ideal, preferably three lines max</p>
  <div class="next">Next</div>
  <span class="corner" style="left:14px">X1</span>
  <svg style="position:absolute;left:261px;top:630px" width="22" height="22"><use href="#i-speaker"/></svg>
</section>

<!-- Screen: Memory (foundation words) -->
<section class="phone" style="left:268px;top:625px">
  <div class="status"><span class="time">4:07</span><span class="camera"></span><svg class="signals" width="36" height="12"><use href="#i-signal"/></svg></div>
  <header class="appbar"><svg class="back"><use href="#i-back"/></svg><span class="title">Memory</span><svg class="share"><use href="#i-share"/></svg></header>
  <div class="stats"><span class="fire"><svg width="16" height="16"><use href="#i-fire"/></svg>2</span><span class="stars"><svg width="18" height="18"><use href="#i-star"/></svg>34</span></div>
  <h2 class="section-head">Foundation</h2>
  <svg class="ring" width="38" height="38" viewBox="0 0 38 38">
    <circle cx="19" cy="19" r="16" fill="none" stroke="#e0e0e0" stroke-width="3.5"/>
    <circle cx="19" cy="19" r="16" fill="none" stroke="#5dc9b7" stroke-width="3.5" stroke-dasharray="70.4 100.5" transform="rotate(-90 19 19)"/>
    <text x="19" y="22" text-anchor="middle" font-size="7.5" font-family="Roboto, sans-serif" fill="#5dc9b7">70%</text>
  </svg>
  <div class="word-card" style="left:16px;top:242px">Book</div>
  <div class="word-card" style="left:155px;top:242px">Door</div>
  <div class="word-card" style="left:16px;top:392px">Hand</div>
  <div class="word-card" style="left:155px;top:392px">File</div>
  <div class="word-card" style="left:16px;top:542px">Star</div>
  <div class="word-card" style="left:155px;top:542px">Window</div>
</section>

<!-- Screen: Mind (subjects) -->
<section class="phone" style="left:504px;top:625px">
  <div class="status"><span class="time">4:07</span><span class="camera"></span><svg class="signals" width="36" height="12"><use href="#i-signal"/></svg></div>
  <header class="appbar"><svg class="back"><use href="#i-back"/></svg><span class="title">Mind</span><svg class="share"><use href="#i-share"/></svg></header>
  <div class="stats"><span class="fire"><svg width="16" height="16"><use href="#i-fire"/></svg>2</span><span class="stars"><svg width="18" height="18"><use href="#i-star"/></svg>34</span></div>
  <div class="progress"><i style="width:36%"></i></div>

  <div class="category" style="top:200px">
    <span class="name">Memory</span><span class="count"><svg width="9" height="9"><use href="#i-star"/></svg>7</span>
    <div class="lesson" style="left:0"><span class="rate"><svg width="8" height="8"><use href="#i-star"/></svg>2</span>Basic<br>Memory</div>
    <div class="lesson" style="left:120px"><span class="rate"><svg width="8" height="8"><use href="#i-star"/></svg>1</span>Names</div>
    <div class="lesson" style="left:240px">Numbers</div>
  </div>
  <div class="category" style="top:337px">
    <span class="name">Dreams</span><span class="count"><svg width="9" height="9"><use href="#i-star"/></svg>7</span>
    <div class="lesson" style="left:0"><span class="rate"><svg width="8" height="8"><use href="#i-star"/></svg>2</span>Basic<br>Memory</div>
    <div class="lesson" style="left:120px"><span class="rate"><svg width="8" height="8"><use href="#i-star"/></svg>1</span>Names</div>
    <div class="lesson" style="left:240px">Numbers</div>
  </div>
  <div class="category" style="top:474px">
    <span class="name">Sub-Concious</span><span class="count"><svg width="9" height="9"><use href="#i-star"/></svg>7</span>
    <div class="lesson" style="left:0"><span class="rate"><svg width="8" height="8"><use href="#i-star"/></svg>2</span>Basic<br>Memory</div>
    <div class="lesson" style="left:120px"><span class="rate"><svg width="8" height="8"><use href="#i-star"/></svg>1</span>Names</div>
    <div class="lesson" style="left:240px">Numbers</div>
  </div>
  <div class="category" style="top:611px">
    <span class="name">Feelings</span><span class="count"><svg width="9" height="9"><use href="#i-star"/></svg>7</span>
    <div class="lesson" style="left:0"><span class="rate"><svg width="8" height="8"><use href="#i-star"/></svg>2</span></div>
    <div class="lesson" style="left:120px"><span class="rate"><svg width="8" height="8"><use href="#i-star"/></svg>1</span></div>
    <div class="lesson" style="left:240px"></div>
  </div>
</section>

<!-- Screen: Memory Test -->
<section class="phone" style="left:745px;top:625px">
  <div class="status"><span class="time">4:07</span><span class="camera"></span><svg class="signals" width="36" height="12"><use href="#i-signal"/></svg></div>
  <header class="appbar"><svg class="back"><use href="#i-back"/></svg><span class="title">Memory Test</span><svg class="share"><use href="#i-share"/></svg></header>
  <div class="stats"><span class="fire"><svg width="16" height="16"><use href="#i-fire"/></svg>2</span><span class="stars"><svg width="18" height="18"><use href="#i-star"/></svg>34</span></div>
  <div class="progress"><i style="width:70%"></i></div>
  <p class="prompt" style="top:236px;left:42px;width:217px">Question Text goes here. Two or three lines</p>
  <p class="kicker" style="top:330px">If it needs further explanation, a kicker of this font size would be ideal, preferably three lines max</p>
  <div class="answer" style="left:26px">Answer<br>1</div>
  <div class="answer" style="left:114px">Answer<br>2</div>
  <div class="answer" style="left:202px">Answer<br>3</div>
  <span class="corner" style="left:14px">X1</span>
  <svg style="position:absolute;left:261px;top:630px" width="22" height="22"><use href="#i-speaker"/></svg>
</section>

</body>
</html>
```